Birthday Calendar: Dec 1 - Nov 30

This calendar should have three parts. First the center should contain an annual calendar beginning December 1, 2019 and going through November 30, 2020. I'm picturing the months and date numbers - no need for individual boxes for each day. Second, above the calendar should be blank space (intended for people to write words of advise and love). Third, beneath the calendar space will be several statements about the year (i.e. "If you have client meetings four times a month, you'll meet with 36 clients." "If you kiss your kids only once each day, that's 1,460 kisses.") I don't have an exact overall size of the calendar in mind, but definitely know it will need to be bigger than 8.5"x11"

Target Market(s)

Wife - Her birthday is November 30, so this is a calendar to mark the time from one birthday to the next.

Font styles to use
Serif

Colors

Designer to choose colors to be used in the design.

Requirements
Must have
• The three different sections listed in the description. There will be 12 people handwriting simple phrases of advise (for how to have the best year) at the top, so there should be enough room for that. At the top it should say "These are the Days"
• I will provide the complete set of statements that will appear at the bottom of the calendar. There will be 10 (or less) statements total, sort of like the ones provided in the description. Let me know when you want those statements.

```html
<!DOCTYPE html>
<html lang="en">
<head>
<meta charset="utf-8">
<title>These are the Days – Birthday Calendar</title>
<link href="https://fonts.googleapis.com/css2?family=Bodoni+Moda:wght@400;600;700&family=Libre+Bodoni:wght@400;700&display=swap" rel="stylesheet">
<style>
  :root{
    --plum:#8c0b4f;
    --plum-soft:#9a2a62;
    --sunday:#c2337a;
    --quote:#f3c3d8;
    --bg-top:#fcf1f6;
    --bg-mid:#f8d6e6;
    --bg-bottom:#f2a8c8;
    --bubble:rgba(255,255,255,.45);
  }
  *{box-sizing:border-box;margin:0;padding:0}
  html,body{width:825px;height:1200px;overflow:hidden}
  body{font-family:"Libre Bodoni",Georgia,serif;color:var(--plum)}
  .poster{
    position:relative;width:825px;height:1200px;overflow:hidden;
    background:linear-gradient(180deg,var(--bg-top) 0%,var(--bg-mid) 55%,var(--bg-bottom) 100%);
  }
  .foliage{position:absolute;border-radius:50%;
    background:radial-gradient(closest-side,rgba(255,255,255,.7),rgba(255,255,255,0))}
  .foliage--top{right:-40px;top:-30px;width:330px;height:170px}
  .foliage--left{left:-60px;top:170px;width:260px;height:230px}
  .swoosh{position:absolute;left:0;top:820px;width:825px;height:380px}
  .title{
    position:absolute;top:40px;left:0;width:825px;text-align:center;
    font-family:"Bodoni Moda",Georgia,serif;font-weight:400;font-size:35px;color:var(--plum);
  }
  .title .q{color:var(--quote);font-size:58px;line-height:0;position:relative;top:14px}
  .frame{position:absolute;left:0;top:0;width:825px;height:660px}
  .notes-area{position:absolute;left:50px;top:100px;width:725px;height:510px}

  .month{position:absolute;width:110px}
  .month h2{font-family:"Bodoni Moda",Georgia,serif;font-weight:700;font-size:13px;margin-bottom:1px;color:var(--plum)}
  .days{display:grid;grid-template-columns:repeat(7,15px);font-size:7.6px;line-height:11px;text-align:center;color:#5a2140}
  .days i{font-style:normal}
  .days .s{color:var(--sunday)}
  .days .bday{background:var(--plum);color:#fff;border-radius:50%;width:12px;height:12px;line-height:12px;margin:0 auto;font-weight:700}

  .stat{position:absolute}
  .bubble{position:absolute;border-radius:50%;background:var(--bubble)}
  .num{position:absolute;font-family:"Bodoni Moda",Georgia,serif;font-weight:700;color:var(--plum);line-height:1;white-space:nowrap}
  .txt{position:absolute;font-size:10.5px;line-height:16px;color:var(--plum-soft);white-space:nowrap}
</style>
</head>
<body>
<main class="poster">
  <div class="foliage foliage--top" role="img" aria-label="Faint white leafy branches"></div>
  <div class="foliage foliage--left" role="img" aria-label="Faint white leafy branch"></div>

  <svg class="swoosh" viewBox="0 0 825 380" aria-hidden="true">
    <path d="M0 150 C250 60 520 80 825 20 L825 60 C520 130 260 110 0 200Z" fill="#fff" opacity=".18"/>
    <path d="M0 260 C300 160 560 200 825 120 L825 150 C560 240 300 210 0 300Z" fill="#fff" opacity=".14"/>
    <path d="M0 330 C280 250 580 280 825 230 L825 380 L0 380Z" fill="#ee9cc0" opacity=".25"/>
  </svg>

  <svg class="frame" viewBox="0 0 825 660" aria-hidden="true" fill="none" stroke="#8c0b4f" stroke-width="1.2">
    <path d="M245 66 C170 58 90 60 50 68 C28 78 24 120 28 200 C34 330 30 480 36 600 C40 620 60 620 120 620 C330 622 560 618 760 620 C795 620 802 600 800 560 C796 440 780 300 790 160 C794 100 800 70 760 64 C700 60 640 62 605 60"/>
    <path d="M240 62 C160 60 70 56 38 74 C22 100 30 170 26 260 C22 380 40 500 30 590 C34 630 80 628 200 626 C420 630 640 624 770 628 C806 624 808 590 804 520 C798 400 798 260 796 140 C794 80 786 58 730 58 C690 58 640 60 600 62"/>
    <path d="M250 70 C180 64 110 68 60 62 C32 66 34 140 34 240 C36 360 22 470 32 570 C36 612 52 616 140 614 C360 616 600 614 750 616 C790 614 796 596 796 540 C794 420 790 300 800 180 C802 110 796 72 770 70 C710 66 650 66 610 66"/>
  </svg>

  <h1 class="title"><span class="q">“</span>These are the Days<span class="q">”</span></h1>
  <div class="notes-area" aria-label="Space for handwritten advice"></div>

  <section class="calendar" aria-label="December 2019 to November 2020">
    <div class="month" style="left:38px;top:666px"><h2>Dec 2019</h2><div class="days">
      <i class="s">1</i><i>2</i><i>3</i><i>4</i><i>5</i><i>6</i><i>7</i><i class="s">8</i><i>9</i><i>10</i><i>11</i><i>12</i><i>13</i><i>14</i><i class="s">15</i><i>16</i><i>17</i><i>18</i><i>19</i><i>20</i><i>21</i><i class="s">22</i><i>23</i><i>24</i><i>25</i><i>26</i><i>27</i><i>28</i><i class="s">29</i><i>30</i><i>31</i></div></div>

    <div class="month" style="left:168px;top:666px"><h2>Jan 2020</h2><div class="days">
      <i style="grid-column-start:4">1</i><i>2</i><i>3</i><i>4</i><i class="s">5</i><i>6</i><i>7</i><i>8</i><i>9</i><i>10</i><i>11</i><i class="s">12</i><i>13</i><i>14</i><i>15</i><i>16</i><i>17</i><i>18</i><i class="s">19</i><i>20</i><i>21</i><i>22</i><i>23</i><i>24</i><i>25</i><i class="s">26</i><i>27</i><i>28</i><i>29</i><i>30</i><i>31</i></div></div>

    <div class="month" style="left:300px;top:666px"><h2>Feb 2020</h2><div class="days">
      <i style="grid-column-start:7">1</i><i class="s">2</i><i>3</i><i>4</i><i>5</i><i>6</i><i>7</i><i>8</i><i class="s">9</i><i>10</i><i>11</i><i>12</i><i>13</i><i>14</i><i>15</i><i class="s">16</i><i>17</i><i>18</i><i>19</i><i>20</i><i>21</i><i>22</i><i class="s">23</i><i>24</i><i>25</i><i>26</i><i>27</i><i>28</i><i>29</i></div></div>

    <div class="month" style="left:432px;top:666px"><h2>Mar 2020</h2><div class="days">
      <i class="s">1</i><i>2</i><i>3</i><i>4</i><i>5</i><i>6</i><i>7</i><i class="s">8</i><i>9</i><i>10</i><i>11</i><i>12</i><i>13</i><i>14</i><i class="s">15</i><i>16</i><i>17</i><i>18</i><i>19</i><i>20</i><i>21</i><i class="s">22</i><i>23</i><i>24</i><i>25</i><i>26</i><i>27</i><i>28</i><i class="s">29</i><i>30</i><i>31</i></div></div>

    <div class="month" style="left:564px;top:666px"><h2>Apr 2020</h2><div class="days">
      <i style="grid-column-start:4">1</i><i>2</i><i>3</i><i>4</i><i class="s">5</i><i>6</i><i>7</i><i>8</i><i>9</i><i>10</i><i>11</i><i class="s">12</i><i>13</i><i>14</i><i>15</i><i>16</i><i>17</i><i>18</i><i class="s">19</i><i>20</i><i>21</i><i>22</i><i>23</i><i>24</i><i>25</i><i class="s">26</i><i>27</i><i>28</i><i>29</i><i>30</i></div></div>

    <div class="month" style="left:694px;top:666px"><h2>May 2020</h2><div class="days">
      <i style="grid-column-start:6">1</i><i>2</i><i class="s">3</i><i>4</i><i>5</i><i>6</i><i>7</i><i>8</i><i>9</i><i class="s">10</i><i>11</i><i>12</i><i>13</i><i>14</i><i>15</i><i>16</i><i class="s">17</i><i>18</i><i>19</i><i>20</i><i>21</i><i>22</i><i>23</i><i class="s">24</i><i>25</i><i>26</i><i>27</i><i>28</i><i>29</i><i>30</i><i class="s">31</i></div></div>

    <div class="month" style="left:36px;top:764px"><h2>Jun 2020</h2><div class="days">
      <i style="grid-column-start:2">1</i><i>2</i><i>3</i><i>4</i><i>5</i><i>6</i><i class="s">7</i><i>8</i><i>9</i><i>10</i><i>11</i><i>12</i><i>13</i><i class="s">14</i><i>15</i><i>16</i><i>17</i><i>18</i><i>19</i><i>20</i><i class="s">21</i><i>22</i><i>23</i><i>24</i><i>25</i><i>26</i><i>27</i><i class="s">28</i><i>29</i><i>30</i></div></div>

    <div class="month" style="left:168px;top:764px"><h2>Jul 2020</h2><div class="days">
      <i style="grid-column-start:4">1</i><i>2</i><i>3</i><i>4</i><i class="s">5</i><i>6</i><i>7</i><i>8</i><i>9</i><i>10</i><i>11</i><i class="s">12</i><i>13</i><i>14</i><i>15</i><i>16</i><i>17</i><i>18</i><i class="s">19</i><i>20</i><i>21</i><i>22</i><i>23</i><i>24</i><i>25</i><i class="s">26</i><i>27</i><i>28</i><i>29</i><i>30</i><i>31</i></div></div>

    <div class="month" style="left:300px;top:764px"><h2>Aug 2020</h2><div class="days">
      <i style="grid-column-start:7">1</i><i class="s">2</i><i>3</i><i>4</i><i>5</i><i>6</i><i>7</i><i>8</i><i class="s">9</i><i>10</i><i>11</i><i>12</i><i>13</i><i>14</i><i>15</i><i class="s">16</i><i>17</i><i>18</i><i>19</i><i>20</i><i>21</i><i>22</i><i class="s">23</i><i>24</i><i>25</i><i>26</i><i>27</i><i>28</i><i>29</i><i class="s">30</i><i>31</i></div></div>

    <div class="month" style="left:432px;top:764px"><h2>Sep 2020</h2><div class="days">
      <i style="grid-column-start:3">1</i><i>2</i><i>3</i><i>4</i><i>5</i><i class="s">6</i><i>7</i><i>8</i><i>9</i><i>10</i><i>11</i><i>12</i><i class="s">13</i><i>14</i><i>15</i><i>16</i><i>17</i><i>18</i><i>19</i><i class="s">20</i><i>21</i><i>22</i><i>23</i><i>24</i><i>25</i><i>26</i><i class="s">27</i><i>28</i><i>29</i><i>30</i></div></div>

    <div class="month" style="left:564px;top:764px"><h2>Oct 2020</h2><div class="days">
      <i style="grid-column-start:5">1</i><i>2</i><i>3</i><i class="s">4</i><i>5</i><i>6</i><i>7</i><i>8</i><i>9</i><i>10</i><i class="s">11</i><i>12</i><i>13</i><i>14</i><i>15</i><i>16</i><i>17</i><i class="s">18</i><i>19</i><i>20</i><i>21</i><i>22</i><i>23</i><i>24</i><i class="s">25</i><i>26</i><i>27</i><i>28</i><i>29</i><i>30</i><i>31</i></div></div>

    <div class="month" style="left:694px;top:764px"><h2>Nov 2020</h2><div class="days">
      <i class="s">1</i><i>2</i><i>3</i><i>4</i><i>5</i><i>6</i><i>7</i><i class="s">8</i><i>9</i><i>10</i><i>11</i><i>12</i><i>13</i><i>14</i><i class="s">15</i><i>16</i><i>17</i><i>18</i><i>19</i><i>20</i><i>21</i><i class="s">22</i><i>23</i><i>24</i><i>25</i><i>26</i><i>27</i><i>28</i><i class="s">29</i><i class="bday">30</i></div></div>
  </section>

  <section class="stats" aria-label="The year in numbers">
    <div class="stat">
      <span class="bubble" style="left:162px;top:864px;width:88px;height:88px"></span>
      <span class="num" style="left:176px;top:866px;font-size:50px">24</span>
      <span class="txt" style="left:166px;top:920px">the number of cups of coffee shared with your parents</span>
      <span class="txt" style="left:188px;top:936px">if they come over twice a month.</span>
    </div>
    <div class="stat">
      <span class="bubble" style="left:494px;top:876px;width:72px;height:72px"></span>
      <span class="num" style="left:502px;top:890px;font-size:34px">156</span>
      <span class="txt" style="left:564px;top:905px">the number of workouts you can squeeze in</span>
      <span class="txt" style="left:532px;top:921px">if you just do it three times a week.</span>
    </div>
    <div class="stat">
      <span class="bubble" style="left:50px;top:952px;width:80px;height:80px"></span>
      <span class="num" style="left:60px;top:964px;font-size:32px">1,460</span>
      <span class="txt" style="left:88px;top:995px;font-size:15px;line-height:18px">the number of kisses given if you kiss each kid just once a day.</span>
    </div>
    <div class="stat">
      <span class="bubble" style="left:570px;top:966px;width:76px;height:76px"></span>
      <span class="num" style="left:578px;top:980px;font-size:46px">20</span>
      <span class="txt" style="left:638px;top:999px">about the number of dates</span>
      <span class="txt" style="left:625px;top:1015px">you could go on with Casey</span>
      <span class="txt" style="left:602px;top:1031px">if you got out every few weeks.</span>
    </div>
    <div class="stat">
      <span class="bubble" style="left:214px;top:1026px;width:60px;height:60px"></span>
      <span class="num" style="left:226px;top:1042px;font-size:28px">12</span>
      <span class="txt" style="left:264px;top:1053px">the number of events you’ll run</span>
      <span class="txt" style="left:242px;top:1068px">if you coordinate one each month.</span>
    </div>
    <div class="stat">
      <span class="bubble" style="left:480px;top:1048px;width:72px;height:72px"></span>
      <span class="num" style="left:494px;top:1070px;font-size:28px">52</span>
      <span class="txt" style="left:532px;top:1081px">the people you’ve made time for</span>
      <span class="txt" style="left:502px;top:1096px">if you meet with just one friend each week.</span>
    </div>
    <div class="stat">
      <span class="bubble" style="left:82px;top:1092px;width:76px;height:76px"></span>
      <span class="num" style="left:90px;top:1100px;font-size:66px">4</span>
      <span class="txt" style="left:130px;top:1102px">the number of days</span>
      <span class="txt" style="left:130px;top:1118px">devoted entirely to you,</span>
      <span class="txt" style="left:130px;top:1134px">if you take two hours a week</span>
      <span class="txt" style="left:130px;top:1150px">just for yourself.</span>
    </div>
    <div class="stat">
      <span class="bubble" style="left:328px;top:1092px;width:80px;height:80px"></span>
      <span class="num" style="left:344px;top:1112px;font-size:30px">260</span>
      <span class="txt" style="left:354px;top:1140px">the number of family meals shared together if you have just 5 dinners a week.</span>
    </div>
  </section>
</main>
</body>
</html>
```